How likely are people to engage in social distancing? We need a good illustration to show the data!

We surveyed U.S. adults March 20th - 24th, 2020 and asked how likely they were to engage in social distancing (and other COVID-19 related health behaviors). What did the survey find? Basically, most people intend to engage in social distancing behaviors (e.g., avoiding large crowds) and other behaviors that reduce the spread of COVID-19 (e.g., washing hands at least 20 seconds). When most people intend to engage in a behavior, then public health professionals try to leverage that to move more people to act.
Now we need innovative and professional images that attempt to communicate one or all of these findings. The specific findings are nicely summarized in the attached document. For example, 82% of participants intend to engage in social distancing.
What sort of visual are we looking for? Our preference is for an original illustration (or set of illustrations). Our preference is for (creative and powerful illustrations, but we are also open to the creative and well-executed infographics.
We need these images fast . We will award monetary prizes to the 3 best designs. If we like more than that, then we might purchase more (e.g., in past contests, we have purchased as many as 30 designs).
What we will need:
(1) The illustrations must be original and we will need the photoshop and/or illustrator files for all artwork.
(2) You can illustrate all of the findings or just one of them. We need creative approaches that do a lucid job of bringing the data to life. Most people intend to engage in these behaviors. How to communicate that? Corvantists and Halmerites do not differ in their intentions; how to communicate that?
(3) The illustration should say, somewhere: "Based on a survey of 400 U.S. adults conducted March 20 - 24th, 2020."

U.S. Adults

• Original illustrations based on the findings of the survey (see attached document).

```html
<!DOCTYPE html>
<html lang="en">
<head>
<meta charset="utf-8">
<title>Social Distancing Intentions Survey</title>
<link rel="stylesheet" href="https://fonts.googleapis.com/css2?family=Nunito:wght@800&family=Oswald:wght@500;600&display=swap">
<style>
  :root {
    --ink: #234b52;
    --navy: #1d4a78;
    --red: #b3303a;
    --teal: #4fc2b4;
    --teal-deep: #3aa8a6;
    --panel: #e4fbfb;
    --panel-line: #4fc2b4;
    --cream: #fbf3e3;
    --rep-col: #fdd1d4;
    --dem-col: #d0eaea;
    --rep-head: #dc1010;
    --dem-head: #0b2fc6;
    --rule: #8a8f8f;
  }
  * { box-sizing: border-box; margin: 0; padding: 0; }
  html, body { width: 1046px; height: 1200px; overflow: hidden; background: #fff; }
  .canvas { position: relative; width: 1046px; height: 1200px; overflow: hidden; background: var(--cream); }

  .title-band { position: absolute; left: 0; top: 0; width: 1046px; height: 57px; background: #fff;
    display: flex; align-items: center; justify-content: center; }
  .title-band h1 { font-family: "Nunito", sans-serif; font-weight: 800; font-size: 26px; color: var(--ink); letter-spacing: 0.1px; }

  .scene-band { position: absolute; left: 0; top: 57px; width: 1046px; height: 588px;
    background: linear-gradient(180deg, var(--teal) 0%, var(--teal) 82%, #bfe8e4 93%, var(--cream) 100%); }
  .home-office-art { position: absolute; left: 0; top: 40px; width: 700px; height: 545px;
    background: radial-gradient(ellipse at 45% 55%, #f0a14a 0%, #3f8ea0 45%, #2f6f86 70%, rgba(79,194,180,0) 100%); opacity: 0.85; }

  .overall-panel { position: absolute; left: 708px; top: 73px; width: 299px; height: 520px;
    background: linear-gradient(180deg, var(--panel) 0%, var(--panel) 72%, rgba(228,251,251,0) 100%); }
  .overall-panel h2 { font-family: "Oswald", sans-serif; font-weight: 600; font-size: 16.5px; line-height: 18px;
    color: var(--navy); padding: 24px 0 0 19px; height: 67px; letter-spacing: 0.2px; }
  .overall-row { display: flex; align-items: center; justify-content: space-between; height: 41.3px;
    border-top: 2px solid var(--panel-line); padding: 0 32px 0 18px; }
  .overall-row:last-child { border-bottom: 2px solid var(--panel-line); }
  .overall-row .label { font-family: "Oswald", sans-serif; font-weight: 500; font-size: 13.5px; line-height: 14.5px; letter-spacing: 0.2px; }
  .overall-row .value { font-family: "Oswald", sans-serif; font-weight: 600; font-size: 27px; }

  .is-blue { color: var(--navy); }
  .is-red { color: var(--red); }

  .elephant-art { position: absolute; left: 0; top: 755px; width: 210px; height: 435px;
    background: #ec5244; border-radius: 90px 110px 0 0; }
  .donkey-art { position: absolute; left: 826px; top: 740px; width: 220px; height: 450px;
    background: #0c6b98; border-radius: 120px 0 0 0; }
  .virus-pattern { position: absolute; left: 0; top: 660px; width: 1046px; height: 540px;
    background: radial-gradient(circle at 20% 12%, rgba(200,214,170,0.7) 0 48px, transparent 49px),
                radial-gradient(circle at 84% 12%, rgba(200,214,170,0.7) 0 48px, transparent 49px); }

  .comparison { position: absolute; left: 237px; top: 707px; width: 591px; height: 440px;
    background: var(--cream); border: 1px solid var(--rule); }
  .col-rep-bg { position: absolute; left: 218px; top: 0; width: 167px; height: 100%; background: var(--rep-col); }
  .col-dem-bg { position: absolute; left: 421px; top: 0; width: 168px; height: 100%; background: var(--dem-col); }
  .comparison-head { position: relative; height: 58px; display: flex; align-items: flex-start; }
  .comparison-head .caption { width: 218px; font-family: "Nunito", sans-serif; font-weight: 800; font-size: 27px; color: var(--ink);
    padding: 1px 0 0 42px; }
  .party { font-family: "Nunito", sans-serif; font-weight: 800; font-size: 23px; color: #fff; height: 39px;
    display: flex; align-items: center; justify-content: center; }
  .party-rep { width: 167px; background: var(--rep-head); }
  .party-dem { width: 168px; background: var(--dem-head); }
  .amp { width: 36px; text-align: center; font-family: "Nunito", sans-serif; font-weight: 800; font-size: 24px; color: var(--ink); line-height: 36px; }
  .comparison-row { position: relative; display: flex; align-items: center; height: 47.5px; border-top: 1px solid var(--rule); }
  .comparison-row .label { width: 218px; padding-left: 12px; font-family: "Oswald", sans-serif; font-weight: 500; font-size: 14.5px; line-height: 15.5px; letter-spacing: 0.2px; }
  .comparison-row .value { font-family: "Oswald", sans-serif; font-weight: 600; font-size: 29px; text-align: center; }
  .comparison-row .rep { width: 167px; }
  .comparison-row .dem { width: 168px; margin-left: 36px; }
  .bottom-line { position: absolute; left: 0; top: 1192px; width: 1046px; height: 3px; background: var(--teal-deep); }
</style>
</head>
<body>
<div class="canvas">
  <header class="title-band">
    <h1>Based on a survey of 400 U.S. adults conducted March 20 - 24th, 2020</h1>
  </header>

  <section class="scene-band">
    <div class="home-office-art" role="img" aria-label="Illustration of a man working from home on a laptop with a cat, a wall clock, a Week 1 note, a window with a virus outside, hand sanitizer and toilet paper rolls on the table"></div>
  </section>

  <section class="overall-panel">
    <h2>PERCENT OF AMERICANS INTENDING<br>TO ENGAGE IN SOCIAL DISTANCING</h2>
    <div class="overall-row is-blue"><span class="label">ENGAGE IN SOCIAL<br>DISTANCING:</span><span class="value">82%</span></div>
    <div class="overall-row is-red"><span class="label">WORK FROM HOME:</span><span class="value">63%</span></div>
    <div class="overall-row is-blue"><span class="label">AVOID LARGE GATHERINGS:</span><span class="value">85%</span></div>
    <div class="overall-row is-red"><span class="label">CANCEL SOCIAL ACTIVITIES:</span><span class="value">81%</span></div>
    <div class="overall-row is-blue"><span class="label">PUT DISTANCE BETWEEN<br>YOURSELF AND OTHER PEOPLE:</span><span class="value">85%</span></div>
    <div class="overall-row is-red"><span class="label">WASH HANDS AT LEAST 20<br>SECONDS</span><span class="value">87%</span></div>
    <div class="overall-row is-blue"><span class="label">USE HAND SANITIZER:</span><span class="value is-red">85%</span></div>
    <div class="overall-row is-red"><span class="label">AVOID TOUCHING YOUR<br>EYES, NOSE, AND MOUTH:</span><span class="value">81%</span></div>
  </section>

  <div class="virus-pattern" role="img" aria-label="Pale green virus particle decorations"></div>
  <div class="elephant-art" role="img" aria-label="Illustration of a red elephant holding a drink"></div>
  <div class="donkey-art" role="img" aria-label="Illustration of a blue donkey holding a drink"></div>

  <section class="comparison">
    <div class="col-rep-bg"></div>
    <div class="col-dem-bg"></div>
    <div class="comparison-head">
      <span class="caption">Comparing</span>
      <span class="party party-rep">Corvantists</span>
      <span class="amp">&amp;</span>
      <span class="party party-dem">Halmerites</span>
    </div>
    <div class="comparison-row is-blue"><span class="label">ENGAGE IN SOCIAL<br>DISTANCING:</span><span class="value rep">82%</span><span class="value dem">81%</span></div>
    <div class="comparison-row is-red"><span class="label">WORK FROM HOME:</span><span class="value rep">60%</span><span class="value dem">65%</span></div>
    <div class="comparison-row is-blue"><span class="label">AVOID LARGE GATHERINGS:</span><span class="value rep">85%</span><span class="value dem">84%</span></div>
    <div class="comparison-row is-red"><span class="label">CANCEL SOCIAL ACTIVITIES:</span><span class="value rep">82%</span><span class="value dem">80%</span></div>
    <div class="comparison-row is-blue"><span class="label">PUT DISTANCE BETWEEN<br>YOURSELF AND OTHER PEOPLE:</span><span class="value rep">84%</span><span class="value dem">87%</span></div>
    <div class="comparison-row is-red"><span class="label">WASH HANDS AT LEAST 20<br>SECONDS</span><span class="value rep">87%</span><span class="value dem">88%</span></div>
    <div class="comparison-row is-blue"><span class="label">USE HAND SANITIZER:</span><span class="value rep">87%</span><span class="value dem">84%</span></div>
    <div class="comparison-row is-red"><span class="label">AVOID TOUCHING YOUR<br>EYES, NOSE, AND MOUTH:</span><span class="value rep">80%</span><span class="value dem">82%</span></div>
  </section>

  <div class="bottom-line"></div>
</div>
</body>
</html>
```